I need a label design for Honey

Tropical Theme Logo designed for a Beekeeping Company.
5 Labels for Honey.
Business Cards
“Sun Orchard”

A Tropical themed logo, either palm tree or bee.

Style of text should be Brush Script italic or something tropical similar.

I like the below style, with no flamingos or pineapples . Colorful and leafy is good, preferably with leaves and flowers that are native to Tropical Queensland Australia.

Label 1. 1 kg rainforest Blend

This will be our standard table honey, I would like to have a vey striking colorful, cheerful design something like to the 2 examples above.

Must have Australian made logo on Side 2 , with words Australian Honey in it. See attached Australian made logo pick either portrait or landscape based on your design.

If you think the attached picture of the Pink Euodia is will help the labels appeal please feel free to use it.
Please See attached Document for content rainforest Honey Label 1 kg.

Barcode 0918273645501

Size of labels ae shown below. I would like 5mm radius on all corners. 15 mm allowance for curvature of bottle.
Side 1 Side 2 Side 3

65mm

Label 2. 1 kg Bloodwood and Scarlet Gum Blend

This will be another of our standard table honey, I would like to have a vey striking colorful, cheerful design something like to the 2 examples above.

Must have Australian made logo on Side 2 , with words Australian Honey in it. See attached Australian made logo pick either portrait or landscape based on your design

If you think the attached picture of the Scarlet Gum is will help the labels appeal please feel free to use it.

Please See attached Document for content Bloodwood and Scarlet Gum Blend Label 1 kg.
Barcode 0918273645518
Side 1 Side 2 Side 3

65mm

Label 3. 500 g rainforest Blend

Exactly the same as the 1 kg rainfest blend but the Net weight ill be changed to 500 grams.

If you think the attached picture of the Pink Euodia is ill help the labels appeal please feel free to use it.
Barcode 0918273645525
Side 1 Side 2 Side 3

65mm

Label 4. 500g Bloodwood and Scarlet Gum Blend

Exactly the same as the 1 kg “Bloodwood and Scarlet Gum Blend” but the Net weight ill be changed to 500 grams.

Barcode 0918273645532
Side 1 Side 2 Side 3

65mm

Label 5. 250g Manuka Honey Attached rough word document for layout and text

This will be our Sun Orchard Premium range of Honeys, A bonze, theme to denote the quality of honey. Printed on silver backed label paper, to give it a shiny appearance.

Main Points
• Bronze backing, see picture below for example from competitor.
• Silver backed labels paper.
• Must have the Australian made Logo on the Front of jar or side 2.
• Side 1 Australian map outline in the bronze backing color with a arrow to Cairns.
• Side 2 has logo “Sun Orchard” Name, Australian Manuka Honey, Leptospermum Polygalifolium Tropicum, Australian Made Logo (Australian Honey) see file “GrownProducedMade_PDF_P (1).pdf”, 250g, NPA+8, MGO 183
• Side 3 TEXT “Our Australian Manuka honey is sourced from pristine native leptospermum forests situated in tropical north Queensland.

Manuka honey gets it’s unique antibacterial properties from naturally occurring methylglyoxal (MGO). The higher the MGO rating the stronger antibacterial properties.”
• Side 4 Nutritional Information Table, Address, Barcode” 0918273645549”, Text “recycled container “with recycled logo

Barcode 0918273645549
First 3 side connected with 6 mm allowance for curvature of bottle, Side 4 separate. 5mm radius on all corners
Side 1 Side 2 Side 3 Side 4

50mm

Competitors labels for inspiration and example of Bronze Backing

*Business Card*
Sun Orchard “logo”

Medical Honey’s
Tropical Rainforest Honeys
Strong 5 Fames Nucleus Colonies all year round
Director Rupert Vasquez
Email: rvasquez.rv@examplemail.test
Mobile no. 0491 058 273
ABN 71596204318

Target Market(s)

Tourist visiting Cairns North Queensland Australia, both foreign mainly Chinese and tourist from Melbourne.

Contact Information for Business Card

Sun Orchard “logo”

Medical Honey’s
Tropical Rainforest Honey's
Director Rupert Vasquez
Mobile no. 0491 058 273
ABN 71596204318

Logo Text

Sun Orchard

Font styles to use
Script

Colors
00a990
f04a50
0255a3
9bcb3b
fbed22

Requirements
Must have
• Clean and Clear, must check all spelling, punctuation and Gram
Nice to have
• Lots of colour in labels but not too much content.
• O
• Manuka labels to be high end looking people are paying good money and should see it in the label.
• Other honey ranges can be colourful and playful. Topical relaxed, rainforest

```html
<!DOCTYPE html>
<html lang="en">
<head>
<meta charset="UTF-8">
<title>Sun Orchard – Bloodwood and Scarlet Gum Blend Label</title>
<link rel="stylesheet" href="https://fonts.googleapis.com/css2?family=Dancing+Script:wght@500;700&family=Open+Sans:wght@700&display=swap">
<style>
  :root {
    --backdrop: #a9a9a9;
    --label-black: #0c0c0c;
    --stripe: #1c1c1c;
    --gold-light: #f4d27a;
    --gold: #d4a236;
    --gold-deep: #a8741c;
    --copper: #7a4a12;
    --leaf-dark: #1e6b2a;
    --leaf-light: #6cc24a;
    --flower-red: #d3140f;
    --flower-deep: #7a0a06;
    --flower-yellow: #f0b23a;
    --net-text: #fff4dc;
  }
  * { box-sizing: border-box; margin: 0; padding: 0; }
  html, body { width: 1200px; height: 1000px; overflow: hidden; }
  body {
    background: radial-gradient(ellipse at center, #c4c4c4 0%, var(--backdrop) 70%);
    position: relative;
  }
  .label {
    position: absolute;
    left: 280px; top: 75px;
    width: 640px; height: 850px;
    background:
      repeating-linear-gradient(90deg, var(--label-black) 0 7px, var(--stripe) 7px 9px);
    overflow: hidden;
  }
  .gold-band {
    position: absolute; left: 0; width: 100%;
    background: linear-gradient(90deg, var(--copper) 0%, var(--gold-deep) 12%, var(--gold-light) 35%, var(--gold) 55%, var(--gold-deep) 80%, var(--copper) 100%);
  }
  .gold-band--top { top: 0; height: 29px; }
  .gold-band--bottom {
    top: 782px; height: 68px;
    display: flex; align-items: center; justify-content: center;
  }
  .net-weight {
    font-family: "Open Sans", Arial, sans-serif;
    font-weight: 700; font-size: 34px;
    color: var(--net-text);
    letter-spacing: 1px;
    text-shadow: 0 1px 2px rgba(60,30,0,.6);
  }
  .leaf-border {
    position: absolute; top: 29px; left: 0; width: 100%; height: 85px;
    background: linear-gradient(180deg, var(--leaf-dark) 0%, var(--leaf-light) 55%, var(--label-black) 100%);
  }
  .brand {
    position: absolute; top: 165px; left: 0; width: 100%;
    display: flex; align-items: center; justify-content: center; gap: 16px;
  }
  .brand-mark {
    width: 58px; height: 58px; border-radius: 50%;
    background: var(--gold);
  }
  .brand-name {
    font-family: "Dancing Script", cursive;
    font-weight: 700; font-size: 44px;
    color: var(--gold);
  }
  .title {
    position: absolute; left: 0; width: 100%;
    text-align: center;
    font-family: "Dancing Script", cursive;
    font-weight: 700;
    background: linear-gradient(180deg, var(--gold-light) 0%, var(--gold) 50%, var(--gold-deep) 100%);
    -webkit-background-clip: text; background-clip: text;
    color: transparent;
    line-height: 1;
  }
  .title--primary { top: 275px; font-size: 104px; }
  .title--joiner { top: 395px; font-size: 36px; font-weight: 500; }
  .title--secondary { top: 432px; font-size: 100px; }
  .blend-line {
    position: absolute; top: 540px; left: 60px; width: 520px;
    display: flex; align-items: center; gap: 14px;
  }
  .blend-line::before, .blend-line::after {
    content: ""; flex: 1; height: 2px; background: var(--gold);
  }
  .blend-word {
    font-family: "Dancing Script", cursive;
    font-weight: 700; font-size: 40px; line-height: 1;
    color: var(--gold);
  }
  .flower-photo {
    position: absolute; top: 590px; left: 22px; width: 596px; height: 192px;
    background: radial-gradient(circle at 30% 55%, var(--flower-yellow) 0 4%, var(--flower-red) 12%, var(--flower-deep) 70%);
  }
</style>
</head>
<body>
  <main class="label">
    <div class="gold-band gold-band--top"></div>
    <div class="leaf-border" role="img" aria-label="Border of tropical rainforest leaves along the top edge"></div>

    <div class="brand">
      <span class="brand-mark"></span>
      <span class="brand-name">Sun Orchard</span>
    </div>

    <h1 class="title title--primary">Bloodwood</h1>
    <p class="title title--joiner">and</p>
    <p class="title title--secondary">Scarlet Gum</p>
    <div class="blend-line"><span class="blend-word">Blend</span></div>

    <div class="flower-photo" role="img" aria-label="Close-up photograph of red scarlet gum blossoms"></div>

    <div class="gold-band gold-band--bottom">
      <span class="net-weight">1 Kg Net</span>
    </div>
  </main>
</body>
</html>
```